Create a website in Wordpress for an interior design company

Create a website for our interior design company 'Roomora'

-Color preferences - Neutral and warm colors. Nothing too bright
-Aesthetic: Modern, Minimalist, Classic, Mature, Luxury
-Mission Statement: Transforming homes into personalized dream spaces through exceptional interior design, meticulous attention to detail, and a touch of the unexpected.
-Brand Values: innovation, creativity, passion and sustainability

Examples: https://www.lenamarchwoodinteriors.com.au/
https://www.tidecraftstudio.com/

About
Portfolio
Inquire page

```html
<!DOCTYPE html>
<html lang="en">
<head>
<meta charset="utf-8">
<title>Roomora — Modern Interior Design Company</title>
<link href="https://fonts.googleapis.com/css2?family=Raleway:wght@500;600;700&family=Montserrat:wght@400;500;600;700&family=Poppins:wght@500;600&display=swap" rel="stylesheet">
<style>
:root{
  --gold:#cf9550;
  --gold-dark:#b97f3c;
  --ink:#111111;
  --text:#2a2a2a;
  --muted:#3d3d3d;
  --cream:#fbf5ee;
  --white:#ffffff;
  --footer:#0b0b0b;
  --footer-bottom:#1a1a1a;
}
*{margin:0;padding:0;box-sizing:border-box}
html,body{width:1200px;height:4724px;overflow:hidden;background:var(--white)}
body{font-family:"Montserrat",sans-serif;color:var(--text)}
.page{position:relative;width:1200px;height:4724px;overflow:hidden}
.abs{position:absolute}
.photo{position:absolute}

/* Header */
.site-header{position:absolute;left:0;top:0;width:1200px;height:105px;background:rgba(40,34,28,.72);z-index:3}
.logo{position:absolute;left:68px;top:34px;font-family:"Raleway",sans-serif;font-weight:600;font-size:38px;color:var(--white);line-height:1}
.main-nav a{position:absolute;top:48px;font-size:13px;font-weight:500;color:var(--white);text-decoration:none;letter-spacing:.3px}
.main-nav a.active{color:var(--gold)}
.main-nav a.active::after{content:"";position:absolute;left:0;right:0;top:24px;height:2px;background:var(--gold)}
.btn{position:absolute;display:flex;align-items:center;justify-content:center;font-family:"Montserrat",sans-serif;font-weight:700;text-decoration:none;letter-spacing:.3px}
.btn-solid{background:var(--gold);color:var(--white)}
.btn-outline{border:2px solid var(--gold);color:var(--gold);background:transparent}

/* Hero */
.hero{position:absolute;left:0;top:0;width:1200px;height:921px;background:linear-gradient(180deg,#b8a286 0%,#d9c7ae 25%,#ece0cf 50%,#f8f0e6 70%,var(--cream) 100%)}
.slider-arrow{position:absolute;top:462px;width:34px;height:34px;border-radius:50%;background:var(--white);display:flex;align-items:center;justify-content:center}
.welcome-pill{position:absolute;left:428px;top:596px;width:345px;height:37px;border-radius:19px;background:var(--ink);color:var(--white);font-family:"Raleway",sans-serif;font-weight:600;font-size:23px;display:flex;align-items:center;justify-content:center}
.hero-title{position:absolute;left:0;width:1200px;top:652px;text-align:center;font-family:"Raleway",sans-serif;font-weight:600;font-size:51px;color:var(--ink);letter-spacing:.5px}

/* Feature cards */
.feature-card{position:absolute;top:1028px;width:299px;height:312px;background:var(--white);box-shadow:0 2px 14px rgba(0,0,0,.14);text-align:center}
.feature-icon{position:absolute;left:95px;top:35px;width:110px;height:110px;border-radius:50%;background:var(--gold);display:flex;align-items:center;justify-content:center}
.feature-title{position:absolute;left:0;right:0;top:170px;font-weight:600;font-size:19px;color:var(--ink)}
.feature-text{position:absolute;left:30px;right:30px;top:210px;font-size:14px;line-height:23px;color:var(--muted);text-align:justify;text-align-last:center}

/* About */
.about-block{position:absolute;left:0;top:1464px;width:486px;height:582px;background:var(--gold)}
.about-frame{position:absolute;left:70px;top:1549px;width:475px;height:420px;background:var(--white);padding:9px}
.about-frame .photo{left:9px;top:9px;width:457px;height:402px;background:linear-gradient(135deg,#efe9e2 0%,#d9cfc4 45%,#b88a55 70%,#8a7d72 100%)}
.section-rule{position:absolute;width:2px;background:var(--gold)}
.section-rule::after{content:"";position:absolute;left:-4px;bottom:-5px;width:10px;height:10px;border-radius:50%;background:var(--gold)}
.section-title{position:absolute;font-family:"Raleway",sans-serif;font-weight:500;font-size:48px;color:var(--ink);line-height:1}
.about-text{position:absolute;left:615px;top:1662px;width:473px;font-size:14px;line-height:26.6px;color:var(--muted);text-align:justify}

/* Services */
.service-card{position:absolute;top:2171px;width:521px;height:369px;overflow:hidden}
.service-card .photo{inset:0}
.service-label{position:absolute;left:0;right:0;bottom:0;height:109px;background:rgba(40,36,32,.55);display:flex;align-items:center;justify-content:center;font-family:"Poppins",sans-serif;font-weight:600;font-size:28px;color:var(--white)}

/* Portfolio */
.portfolio-item{position:absolute;border-radius:3px}

/* Video */
.video-band{position:absolute;left:0;top:3839px;width:1200px;height:473px;background:linear-gradient(100deg,#6b5a4a 0%,#8c7560 30%,#a58d74 55%,#7a6656 80%,#3e332b 100%)}
.play-button{position:absolute;left:552px;top:4030px;width:92px;height:92px}

/* Footer */
.site-footer{position:absolute;left:0;top:4312px;width:1200px;height:412px;background:var(--footer)}
.footer-logo{position:absolute;left:0;width:1200px;top:4383px;text-align:center;font-family:"Raleway",sans-serif;font-weight:600;font-size:56px;color:var(--white);line-height:1}
.contact-item{position:absolute;top:4505px;display:flex;align-items:center;gap:12px;color:var(--white);font-size:13px;line-height:18px}
.contact-icon{width:28px;height:28px;border-radius:4px;background:var(--gold);display:flex;align-items:center;justify-content:center;flex:none}
.contact-item b{font-weight:700;display:block}
.footer-rule{position:absolute;left:66px;top:4578px;width:1066px;height:1px;background:#3a3a3a}
.footer-nav a{position:absolute;top:4607px;font-size:13px;font-weight:500;color:var(--white);text-decoration:none}
.footer-nav a.active{font-weight:700}
.footer-bottom{position:absolute;left:0;top:4663px;width:1200px;height:61px;background:var(--footer-bottom)}
.copyright{position:absolute;left:66px;top:4688px;font-size:11px;color:var(--white)}
.social-square{position:absolute;top:4683px;width:24px;height:24px;border-radius:3px;background:var(--gold)}
</style>
</head>
<body>
<div class="page">

  <!-- Hero -->
  <section class="hero" role="img" aria-label="Bright modern living room with white sofa, staircase, wall TV and warm lamps"></section>

  <header class="site-header">
    <div class="logo">Roomora</div>
    <nav class="main-nav">
      <a href="#" class="active" style="left:556px">HOME</a>
      <a href="#" style="left:660px">ABOUT US</a>
      <a href="#" style="left:787px">PORTFOLIO</a>
      <a href="#" style="left:920px">CONTACT</a>
    </nav>
    <a href="#" class="btn btn-solid" style="left:1020px;top:35px;width:116px;height:35px;font-size:13px">INQUIRE</a>
  </header>

  <div class="slider-arrow" style="left:67px"><svg width="12" height="12" viewBox="0 0 12 12"><path d="M8 1 3 6l5 5" stroke="#111" stroke-width="2" fill="none"/></svg></div>
  <div class="slider-arrow" style="left:1097px"><svg width="12" height="12" viewBox="0 0 12 12"><path d="M4 1l5 5-5 5" stroke="#111" stroke-width="2" fill="none"/></svg></div>

  <div class="welcome-pill">Welcome To Roomora</div>
  <h1 class="hero-title">MODERN INTERIOR DESIGN COMPANY</h1>
  <a href="#" class="btn btn-solid" style="left:393px;top:754px;width:200px;height:57px;font-size:17px">INQUIRE</a>
  <a href="#" class="btn btn-outline" style="left:607px;top:754px;width:199px;height:57px;font-size:17px">GET STARTED</a>

  <!-- Features -->
  <div class="feature-card" style="left:99px">
    <div class="feature-icon"><svg width="52" height="52" viewBox="0 0 52 52"><path d="M20 8h12l-4 7h-4z" fill="#fff"/><path d="M26 15c-12 0-18 12-18 20 0 7 6 10 18 10s18-3 18-10c0-8-6-20-18-20z" fill="#fff"/><text x="26" y="39" text-anchor="middle" font-family="Montserrat,sans-serif" font-weight="700" font-size="17" fill="#cf9550">$</text></svg></div>
    <div class="feature-title">RESONABLE PRICES</div>
    <p class="feature-text">Lorem ipsum dolor sit amet, consec tetur adipiscing elit.</p>
  </div>
  <div class="feature-card" style="left:450px">
    <div class="feature-icon"><svg width="54" height="54" viewBox="0 0 54 54"><rect x="8" y="8" width="38" height="38" fill="none" stroke="#fff" stroke-width="3"/><circle cx="27" cy="27" r="8" fill="none" stroke="#fff" stroke-width="4"/><circle cx="8" cy="8" r="4" fill="#fff"/><circle cx="46" cy="8" r="4" fill="#fff"/><circle cx="8" cy="46" r="4" fill="#fff"/><circle cx="46" cy="46" r="4" fill="#fff"/></svg></div>
    <div class="feature-title">EXCLUSIVE DESIGN</div>
    <p class="feature-text">Lorem ipsum dolor sit amet, consec tetur adipiscing elit.</p>
  </div>
  <div class="feature-card" style="left:802px">
    <div class="feature-icon"><svg width="60" height="50" viewBox="0 0 60 50"><circle cx="30" cy="14" r="9" fill="#fff"/><path d="M15 46c0-10 7-17 15-17s15 7 15 17z" fill="#fff"/><circle cx="12" cy="18" r="6" fill="#fff"/><circle cx="48" cy="18" r="6" fill="#fff"/><path d="M2 40c0-7 4-12 10-12 3 0 5 1 6 2-3 3-5 6-5 10z" fill="#fff"/><path d="M58 40c0-7-4-12-10-12-3 0-5 1-6 2 3 3 5 6 5 10z" fill="#fff"/></svg></div>
    <div class="feature-title">PROFESSIONAL TEAM</div>
    <p class="feature-text">Lorem ipsum dolor sit amet, consec tetur adipiscing elit.</p>
  </div>

  <!-- About -->
  <div class="about-block"></div>
  <div class="about-frame"><div class="photo" role="img" aria-label="Open-plan living room with white sectional sofa and wood-panelled wall"></div></div>
  <div class="section-rule" style="left:618px;top:1560px;height:66px"></div>
  <h2 class="section-title" style="left:644px;top:1569px">About Us</h2>
  <p class="about-text">Lorem ipsum dolor sit amet, consectetur adipiscing elit. Aliquam at fermentum erat. Suspendisse convallis ultrices efficitur. Suspendisse potenti. Etiam ullamcorper ipsum eu felis feugiat, id fermentum justo rhoncus. Vestibulum laoreet placerat vehicula. Fusce ligula mi, tempor id maximus a, tempus non mi. Vestibulum ante ipsum primis in faucibus orci luctus et ultrices posuere cubilia curae; Aenean scelerisque dolor in urna condimentum volutpat.</p>
  <a href="#" class="btn btn-solid" style="left:618px;top:1885px;width:156px;height:51px;font-size:13px">READ MORE</a>

  <!-- Services -->
  <div class="abs" style="left:53px;top:2156px;width:297px;height:140px;background:var(--gold)"></div>
  <div class="abs" style="left:850px;top:2281px;width:297px;height:273px;background:var(--gold)"></div>
  <div class="service-card" style="left:66px">
    <div class="photo" role="img" aria-label="Residential lounge with beige sofa, orange cushions and round coffee table" style="background:linear-gradient(135deg,#e8ddd0 0%,#c9b59c 50%,#8b6d4d 100%)"></div>
    <div class="service-label">Residential Interior Design</div>
  </div>
  <div class="service-card" style="left:613px">
    <div class="photo" role="img" aria-label="Commercial office space with feature wall, wood table and red chairs" style="background:linear-gradient(135deg,#3a3633 0%,#6c5a4a 45%,#a88a6a 75%,#5b4a3d 100%)"></div>
    <div class="service-label">Commercial Interior Design</div>
  </div>

  <!-- Portfolio -->
  <div class="section-rule" style="left:94px;top:2679px;height:66px"></div>
  <h2 class="section-title" style="left:121px;top:2686px">Our Portfolio</h2>
  <a href="#" class="btn btn-solid" style="left:950px;top:2688px;width:184px;height:59px;font-size:17px">VIEW MORE</a>

  <div class="portfolio-item" style="left:68px;top:2818px;width:525px;height:302px;background:linear-gradient(135deg,#3a2f28 0%,#c08a3e 40%,#e6d4b8 65%,#4a3a30 100%)" role="img" aria-label="Living room with warm wall art, cream sofa and wooden floor"></div>
  <div class="portfolio-item" style="left:607px;top:2818px;width:525px;height:302px;background:linear-gradient(135deg,#d8d6d2 0%,#f2f0ec 45%,#b89a76 80%,#6b5444 100%)" role="img" aria-label="White modern kitchen with island and black bar stools"></div>
  <div class="portfolio-item" style="left:68px;top:3134px;width:343px;height:301px;background:linear-gradient(135deg,#6a6a68 0%,#ebe9e5 50%,#3a3430 100%)" role="img" aria-label="Kitchen dining area with black pendant lights and dark chairs"></div>
  <div class="portfolio-item" style="left:428px;top:3134px;width:343px;height:301px;background:linear-gradient(135deg,#b7652f 0%,#e7e0d6 50%,#c06a35 100%)" role="img" aria-label="Bathroom with timber vanity, mirror and freestanding bath"></div>
  <div class="portfolio-item" style="left:787px;top:3134px;width:345px;height:301px;background:linear-gradient(135deg,#8f8a82 0%,#d6cfc4 45%,#c99a4c 80%,#6f5f4e 100%)" role="img" aria-label="Bathroom with marble vanity top and glass shower"></div>
  <div class="portfolio-item" style="left:68px;top:3452px;width:525px;height:301px;background:linear-gradient(90deg,#a0805e 0%,#b8966f 35%,#e9e6e1 60%,#d8d4ce 100%)" role="img" aria-label="Dining nook with timber slat wall, framed print and white chairs"></div>
  <div class="portfolio-item" style="left:607px;top:3452px;width:525px;height:301px;background:linear-gradient(90deg,#6a4a33 0%,#c9b8a3 40%,#e8ddd0 70%,#8a7a6c 100%)" role="img" aria-label="Bathroom with dark wood vanity and glass shower screen"></div>

  <!-- Video -->
  <section class="video-band" role="img" aria-label="Lounge with leather sofa, stone wall and warm LED strip lighting"></section>
  <svg class="play-button" viewBox="0 0 92 92" aria-label="Play video"><circle cx="46" cy="46" r="42" fill="rgba(0,0,0,.35)" stroke="#fff" stroke-width="5"/><path d="M36 28v36l30-18z" fill="#fff"/></svg>

  <!-- Footer -->
  <footer class="site-footer"></footer>
  <div class="footer-logo">Roomora</div>
  <div class="contact-item" style="left:206px">
    <span class="contact-icon"><svg width="14" height="14" viewBox="0 0 14 14"><path d="M3 1l2.5 3-1.5 1.5c.8 1.8 2 3 3.5 3.5L9 7.5l3 2.5-1.5 2.5C6 12 2 8 1.5 2.5z" fill="#fff"/></svg></span>
    <span><b>CALL US</b>8012 345 6789</span>
  </div>
  <div class="contact-item" style="left:428px">
    <span class="contact-icon"><svg width="14" height="12" viewBox="0 0 14 12"><rect x="1" y="1" width="12" height="10" fill="#fff"/><path d="M1 1l6 5 6-5" stroke="#cf9550" stroke-width="1.4" fill="none"/></svg></span>
    <span><b>EMAIL US</b>info@websitename.com</span>
  </div>
  <div class="contact-item" style="left:724px">
    <span class="contact-icon"><svg width="12" height="16" viewBox="0 0 12 16"><path d="M6 1a5 5 0 0 0-5 5c0 4 5 9 5 9s5-5 5-9a5 5 0 0 0-5-5z" fill="#fff"/><circle cx="6" cy="6" r="2" fill="#cf9550"/></svg></span>
    <span>Address line Dummy Here<br>Address line Here</span>
  </div>
  <div class="footer-rule"></div>
  <nav class="footer-nav">
    <a href="#" class="active" style="left:383px">HOME</a>
    <a href="#" style="left:487px">ABOUT US</a>
    <a href="#" style="left:614px">PORTFOLIO</a>
    <a href="#" style="left:748px">CONTACT</a>
  </nav>
  <div class="footer-bottom"></div>
  <div class="copyright">Copyright © 2024 All Rights Reserved By Comapny Name</div>
  <span class="social-square" style="left:1015px"></span>
  <span class="social-square" style="left:1047px"></span>
  <span class="social-square" style="left:1079px"></span>
  <span class="social-square" style="left:1110px"></span>

</div>
</body>
</html>
```